CRANDEL'S needs a label design for a Moruga Scorpion Pepper Hot Sauce (5oz bottle)

We need a label for a new company based in south Mississippi called CRANDEL'S. We have a new hot sauce made from Moruga Scorpion Peppers that's very hot yet has "layers of flavor". The sauce is a deep red color in a clear bottle. We are looking for something simple yet different and will stand out. We would like to limit the design to 3 colors.

• wide latin?

```html
<!DOCTYPE html>
<html lang="en">
<head>
<meta charset="utf-8">
<title>Crandel's Hot Sauce Label</title>
<link rel="stylesheet" href="https://fonts.googleapis.com/css2?family=Abril+Fatface&family=Libre+Baskerville:wght@400;700&family=Archivo+Narrow:wght@400;700&display=swap">
<style>
  :root {
    --backdrop: #f2f0ee;
    --label-white: #ffffff;
    --pepper-red: #d3261c;
    --ink: #1c1c1c;
  }
  * { margin: 0; padding: 0; box-sizing: border-box; }
  html, body {
    width: 717px;
    height: 1200px;
    overflow: hidden;
    background: var(--backdrop);
  }
  .artboard {
    position: relative;
    width: 717px;
    height: 1200px;
  }
  .front-label {
    position: absolute;
    left: 30px;
    top: 330px;
    width: 460px;
    height: 560px;
    background: var(--label-white);
    box-shadow: 0 2px 10px rgba(0,0,0,0.08);
    display: flex;
    flex-direction: column;
    align-items: center;
    padding-top: 120px;
    color: var(--pepper-red);
    text-align: center;
  }
  .brand-name {
    font-family: "Abril Fatface", serif;
    font-size: 46px;
    line-height: 1;
    letter-spacing: 3px;
  }
  .product-name {
    margin-top: 14px;
    font-family: "Abril Fatface", serif;
    font-size: 68px;
    line-height: 1;
  }
  .heat-band {
    margin-top: 12px;
    width: 380px;
    padding: 8px 0 6px;
    background: var(--pepper-red);
    color: var(--label-white);
    font-family: "Abril Fatface", serif;
    font-size: 34px;
    line-height: 1.1;
    letter-spacing: 2px;
  }
  .established {
    margin-top: 22px;
    font-family: "Libre Baskerville", serif;
    font-size: 22px;
    letter-spacing: 1px;
  }
  .pepper-line {
    margin-top: 14px;
    font-family: "Libre Baskerville", serif;
    font-size: 17px;
    letter-spacing: 2px;
  }
  .net-volume {
    margin-top: auto;
    margin-bottom: 42px;
    font-family: "Libre Baskerville", serif;
    font-size: 15px;
    letter-spacing: 1px;
  }
  .nutrition-panel {
    position: absolute;
    left: 510px;
    top: 420px;
    width: 185px;
    padding: 6px 7px;
    background: var(--label-white);
    border: 2px solid var(--ink);
    font-family: "Archivo Narrow", sans-serif;
    color: var(--ink);
    font-size: 10px;
    line-height: 1.35;
  }
  .nutrition-title {
    font-weight: 700;
    font-size: 21px;
    line-height: 1.05;
    border-bottom: 1px solid var(--ink);
    padding-bottom: 3px;
    margin-bottom: 2px;
  }
  .nutrition-row {
    display: flex;
    justify-content: space-between;
    border-bottom: 1px solid var(--ink);
  }
  .nutrition-row.thick { border-bottom-width: 5px; }
  .nutrition-row.medium { border-bottom-width: 3px; }
  .nutrition-row.last { border-bottom: none; }
  .strong { font-weight: 700; }
</style>
</head>
<body>
<main class="artboard">
  <section class="front-label" aria-label="Crandel's hot sauce front label">
    <div class="brand-name">CRANDEL'S</div>
    <div class="product-name">HOT SAUCE</div>
    <div class="heat-band">VERY HOT!</div>
    <div class="established">EST. 2014</div>
    <div class="pepper-line">MORUGA SCORPION PEPPER</div>
    <div class="net-volume">5 FL. OZ.</div>
  </section>

  <aside class="nutrition-panel" aria-label="Nutrition facts">
    <div class="nutrition-title">Nutrition Facts</div>
    <div>Serving Size 1 tsp (5ml)</div>
    <div class="nutrition-row thick"><span>Servings Per Container 30</span></div>
    <div class="nutrition-row"><span class="strong">Amount Per Serving</span></div>
    <div class="nutrition-row medium"><span class="strong">Calories 0</span></div>
    <div class="nutrition-row"><span></span><span class="strong">Daily Value</span></div>
    <div class="nutrition-row"><span><b>Total Fat</b> 0g</span><span>0%</span></div>
    <div class="nutrition-row"><span><b>Sodium</b> 90mg</span><span>4%</span></div>
    <div class="nutrition-row"><span><b>Total Carbohydrate</b> 0g</span><span>0%</span></div>
    <div class="nutrition-row last"><span><b>Protein</b> 0g</span></div>
  </aside>
</main>
</body>
</html>
```